Professional Business Cards for Recruiting Company

We'd like professional 2-sided business cards that reflect a color scheme that matches our website, www.queryvantline.com, and / or logo that is attached.

Slogan used is "We Know People", but needs to be editable because we change it up to "We Know Developers", "We Speak Geek", etc.

Must includes logo, slogan, first and last name, address, email, mobile number and website address.

Files attached for ideas.

Thanks!

Contact Information for Business Card

Logo, Company name, First name, Last name, addresss, email, phone, website address.

Font styles to use
Sans Serif

Colors
0054AA
0677BA
7BADD7
CADEEF
E8F1F8

Requirements
Nice to have
• I do like the following designs. 22962062 and 22962651. Couple ideas anyway.

```html
<!DOCTYPE html>
<html lang="en">
<head>
<meta charset="utf-8">
<title>Queryvant Business Cards</title>
<link rel="stylesheet" href="https://fonts.googleapis.com/css2?family=Montserrat:wght@300;400;600;700&display=swap">
<style>
  :root {
    --backdrop: #75604a;
    --card-blue: #1d4e8c;
    --card-shadow: rgba(0, 0, 0, 0.45);
    --ink-white: #ffffff;
    --ink-soft: #e8f1f8;
    --accent-faint: rgba(202, 222, 239, 0.18);
  }
  html, body {
    margin: 0;
    padding: 0;
    width: 900px;
    height: 1200px;
    overflow: hidden;
    background: var(--backdrop);
    font-family: "Montserrat", sans-serif;
  }
  .canvas {
    position: relative;
    width: 900px;
    height: 1200px;
  }
  .card {
    position: absolute;
    left: 80px;
    width: 742px;
    height: 440px;
    border-radius: 32px;
    background: var(--card-blue);
    box-shadow: 0 6px 10px var(--card-shadow);
    overflow: hidden;
    color: var(--ink-white);
  }
  .card--front { top: 132px; }
  .card--back { top: 638px; }

  .brand {
    position: absolute;
    display: flex;
    align-items: center;
  }
  .brand__mark {
    border: 2px solid var(--ink-white);
    flex: none;
  }
  .brand__text { display: flex; flex-direction: column; }
  .brand__name {
    font-weight: 300;
    letter-spacing: 1px;
    line-height: 1;
    border-bottom: 2px solid var(--ink-white);
  }
  .brand__tagline {
    font-weight: 600;
    letter-spacing: 0.8px;
    white-space: nowrap;
  }

  .card--front .brand { left: 42px; top: 52px; }
  .card--front .brand__mark { width: 58px; height: 58px; margin-right: 22px; }
  .card--front .brand__name { font-size: 40px; padding-bottom: 4px; }
  .card--front .brand__tagline { font-size: 10px; margin-top: 4px; }

  .front-decoration {
    position: absolute;
    right: -60px;
    top: 30px;
    width: 300px;
    height: 300px;
    border: 4px solid var(--accent-faint);
    background: rgba(123, 173, 215, 0.08);
  }

  .holder { position: absolute; left: 35px; top: 200px; }
  .holder__name { font-size: 25px; font-weight: 700; margin: 0; line-height: 1.1; }
  .holder__title { font-size: 15px; font-weight: 400; margin: 2px 0 0; }

  .address {
    position: absolute;
    left: 35px;
    top: 274px;
    font-size: 15.5px;
    font-style: normal;
    line-height: 21px;
  }

  .contact-list {
    position: absolute;
    left: 34px;
    top: 338px;
    margin: 0;
    padding: 0;
    list-style: none;
    font-size: 15.5px;
    line-height: 22.5px;
  }
  .contact-list li { display: flex; align-items: center; }
  .contact-list svg { width: 14px; height: 14px; margin-right: 13px; fill: var(--ink-white); }

  .card--back .brand { left: 66px; top: 140px; }
  .card--back .brand__mark { width: 110px; height: 110px; margin-right: 60px; }
  .card--back .brand__name { font-size: 64px; padding-bottom: 6px; }
  .card--back .brand__tagline { font-size: 15px; margin-top: 8px; }

  .slogan {
    position: absolute;
    left: 0;
    right: 0;
    top: 376px;
    text-align: center;
    font-size: 16px;
    font-weight: 400;
    letter-spacing: 6px;
    color: var(--ink-soft);
    margin: 0;
  }
</style>
</head>
<body>
<main class="canvas">
  <section class="card card--front" aria-label="Business card front">
    <div class="brand">
      <span class="brand__mark"></span>
      <div class="brand__text">
        <span class="brand__name">QUERYVANT</span>
        <span class="brand__tagline">PROFESSIONAL SOURCING AND RECRUITING</span>
      </div>
    </div>

    <div class="front-decoration" aria-hidden="true"></div>

    <div class="holder">
      <h1 class="holder__name">Dale Hovland</h1>
      <p class="holder__title">President</p>
    </div>

    <address class="address">
      2710 Prairie Lab Loop S<br>
      Fargo, North Dakota 58104
    </address>

    <ul class="contact-list">
      <li>
        <svg viewBox="0 0 16 16" aria-hidden="true"><path d="M2 6c0-2 2-4 6-4s6 2 6 4l-3 1-1-2H6L5 7 2 6zm2 2h8l1 6H3l1-6zm4 1.5a2 2 0 1 0 0 4 2 2 0 0 0 0-4z"/></svg>
        (555) 014-2290
      </li>
      <li>
        <svg viewBox="0 0 16 16" aria-hidden="true"><path d="M1 4h14v1L8 9 1 5V4zm0 3l7 4 7-4v6H1V7z"/></svg>
        support@queryvantline.com
      </li>
      <li>
        <svg viewBox="0 0 16 16" aria-hidden="true"><circle cx="8" cy="8" r="7"/><path d="M5 4c2 0 2 2 4 2s0 3-2 3-1 3-3 2-1-4 0-5zm6 5c1 0 2 1 1 3-1 0-2-1-1-3z" fill="#1d4e8c"/></svg>
        www.queryvantline.com
      </li>
    </ul>
  </section>

  <section class="card card--back" aria-label="Business card back">
    <div class="brand">
      <span class="brand__mark"></span>
      <div class="brand__text">
        <span class="brand__name">QUERYVANT</span>
        <span class="brand__tagline">PROFESSIONAL SOURCING AND RECRUITING</span>
      </div>
    </div>
    <p class="slogan">WE KNOW DEVELOPERS</p>
  </section>
</main>
</body>
</html>
```